Brixelo Photography Business Cards

We need a good general business card that we can hand to our clients. We will be doing embossed gloss cards.

Target Market(s)

Real estate / Business to business / professionals

```html
<!DOCTYPE html>
<html lang="en">
<head>
<meta charset="utf-8">
<title>Brixelo Photography – Business Cards</title>
<link rel="stylesheet" href="https://fonts.googleapis.com/css2?family=Lato:wght@400;700;900&display=swap">
<style>
  :root {
    --backdrop: #2b2b2e;
    --navy: #27236b;
    --navy-deep: #1f1c5c;
    --sky: #3a8fd2;
    --sky-light: #4fc1ec;
    --paper: #ffffff;
    --ink: #1f1f2a;
  }
  * { box-sizing: border-box; margin: 0; padding: 0; }
  html, body { width: 1200px; height: 900px; overflow: hidden; }
  body {
    background: var(--backdrop);
    font-family: "Lato", sans-serif;
    position: relative;
  }
  .card {
    position: absolute;
    width: 560px;
    height: 320px;
    border-radius: 18px;
    overflow: hidden;
  }
  /* Front */
  .card-front {
    left: 60px; top: 90px;
    background: linear-gradient(225deg, var(--sky) 0%, #2f5fae 40%, var(--navy) 75%, var(--navy-deep) 100%);
    color: var(--paper);
  }
  .front-brand {
    position: absolute;
    left: 0; right: 0; top: 118px;
    text-align: center;
    font-weight: 900;
    font-size: 44px;
    letter-spacing: 0.5px;
    color: var(--paper);
  }
  .front-web {
    position: absolute;
    left: 0; right: 0; bottom: 34px;
    text-align: center;
    font-size: 12px;
    letter-spacing: 0.4px;
    color: var(--paper);
  }
  /* Back */
  .card-back {
    left: 580px; top: 470px;
    background: var(--paper);
  }
  .back-wave { position: absolute; inset: 0; }
  .holder {
    position: absolute;
    left: 30px; top: 70px;
    color: var(--paper);
  }
  .holder-name { font-weight: 700; font-size: 19px; }
  .holder-role { font-size: 13px; margin-top: 2px; opacity: 0.9; }
  .contact-list {
    position: absolute;
    left: 30px; top: 190px;
    list-style: none;
    color: var(--ink);
    font-size: 12.5px;
  }
  .contact-item {
    display: flex; align-items: center; gap: 10px;
    min-height: 26px;
  }
  .contact-icon {
    width: 20px; height: 20px;
    border-radius: 4px;
    background: var(--sky-light);
    display: flex; align-items: center; justify-content: center;
    flex: none;
  }
  .contact-address { line-height: 1.2; }
  .back-brand {
    position: absolute;
    right: 34px; top: 110px;
    width: 190px; height: 190px;
    border: 3px solid var(--navy);
    border-radius: 50%;
    display: flex; align-items: center; justify-content: center;
    text-align: center;
    font-weight: 900;
    font-size: 24px;
    line-height: 1.15;
    color: var(--navy);
  }
</style>
</head>
<body>

<section class="card card-front">
  <p class="front-brand">Brixelo Photography</p>
  <p class="front-web">www.brixelophotography.com</p>
</section>

<section class="card card-back">
  <svg class="back-wave" viewBox="0 0 560 320" width="560" height="320" aria-hidden="true">
    <defs>
      <linearGradient id="bandFill" x1="0" y1="1" x2="1" y2="0">
        <stop offset="0" stop-color="#4fc1ec"/>
        <stop offset="0.55" stop-color="#3a8fd2"/>
        <stop offset="1" stop-color="#27236b"/>
      </linearGradient>
    </defs>
    <path d="M0,0 H560 V28 C480,28 400,55 330,100 C250,150 140,150 0,150 Z" fill="url(#bandFill)"/>
    <path d="M0,157 C140,157 255,157 336,106 C405,62 480,38 560,36 V44 C482,46 410,70 342,113 C260,165 140,165 0,165 Z" fill="#4fc1ec"/>
    <path d="M200,0 H560 V14 C470,6 390,25 330,60 C370,25 420,8 470,0 Z" fill="#27236b"/>
  </svg>

  <div class="holder">
    <p class="holder-name">Dorian Vale</p>
    <p class="holder-role">Owner/Photographer</p>
  </div>

  <ul class="contact-list">
    <li class="contact-item">
      <span class="contact-icon">
        <svg width="12" height="12" viewBox="0 0 12 12"><path d="M2.5 1 L4.5 1 L5 3.5 L3.8 4.4 Q4.8 6.8 7.6 8.2 L8.5 7 L11 7.5 L11 9.5 Q10.5 11 9 11 Q1 10 1 2.5 Q1 1 2.5 1 Z" fill="#fff"/></svg>
      </span>
      555-014-2286
    </li>
    <li class="contact-item">
      <span class="contact-icon">
        <svg width="12" height="10" viewBox="0 0 12 10"><rect x="0.5" y="0.5" width="11" height="9" rx="1" fill="#fff"/><path d="M1 1.5 L6 5.5 L11 1.5" stroke="#4fc1ec" stroke-width="1.2" fill="none"/></svg>
      </span>
      info@brixelophotography.com
    </li>
    <li class="contact-item">
      <span class="contact-icon">
        <svg width="12" height="12" viewBox="0 0 12 12"><circle cx="6" cy="6" r="5" fill="none" stroke="#fff" stroke-width="1.2"/><ellipse cx="6" cy="6" rx="2.2" ry="5" fill="none" stroke="#fff" stroke-width="1"/><path d="M1 6 H11" stroke="#fff" stroke-width="1"/></svg>
      </span>
      www.brixelophotography.com
    </li>
    <li class="contact-item">
      <span class="contact-icon">
        <svg width="10" height="13" viewBox="0 0 10 13"><path d="M5 12.5 C2 8.5 0.5 6.5 0.5 4.5 A4.5 4.5 0 0 1 9.5 4.5 C9.5 6.5 8 8.5 5 12.5 Z" fill="#fff"/><circle cx="5" cy="4.6" r="1.6" fill="#4fc1ec"/></svg>
      </span>
      <span class="contact-address">Here is your full address<br>Road no.123, Texas, USA</span>
    </li>
  </ul>

  <p class="back-brand">Brixelo<br>Photography</p>
</section>

</body>
</html>
```